integrative health clinic-Medical massage, acupuncture, chiropractic

we like our logo, but are open to new ideas. We need a new card design. We have added chiropractic and acupuncture that we have put under the name of the business. We are an integrative medical clinic

Target Market(s)

General public, athletes

Contact Information for Business Card

Phone 5055583927
Fax 5055583926
Hours Monday-Friday 9-6
Saturday 10-6
The 20% can be smaller on the back

Colors
3176b5
0355a3

Requirements
Must have
• Logo but am open to ideas
Nice to have
• We are an integrated medical clinic but also want to be personable. We want the card fun and inviting

```html
<!DOCTYPE html>
<html lang="en">
<head>
<meta charset="utf-8">
<title>Open Range Wellness – Business Cards</title>
<link href="https://fonts.googleapis.com/css2?family=Open+Sans:wght@400;600;700&family=Open+Sans+Condensed:wght@700&family=Tinos:ital@1&display=swap" rel="stylesheet">
<style>
  :root {
    --brand-blue: #263c96;
    --brand-tint: #dfe3ef;
    --brand-wash: #eef0f6;
    --ink: #161616;
    --paper: #f7f7f7;
    --paper-edge: #e8e8e8;
    --backdrop: #d9d9d9;
  }
  * { box-sizing: border-box; margin: 0; padding: 0; }
  html, body {
    width: 1200px; height: 1021px; overflow: hidden;
    background: var(--backdrop);
    font-family: "Open Sans", Arial, sans-serif;
    color: var(--ink);
  }
  .sheet {
    position: relative; width: 1200px; height: 1021px;
    display: flex; flex-direction: column; align-items: center; justify-content: center; gap: 44px;
  }
  .card {
    position: relative; width: 760px; height: 434px;
    background: linear-gradient(135deg, #ffffff 0%, var(--paper) 60%, var(--paper-edge) 100%);
    box-shadow: 0 6px 18px rgba(0,0,0,0.18);
    overflow: hidden;
  }

  /* Back of card */
  .brand-disc {
    position: absolute; left: 110px; top: 50px;
    width: 320px; height: 320px; border-radius: 50%;
    background: var(--brand-wash);
  }
  .offer {
    position: absolute; left: 150px; top: 100px; width: 260px;
    color: var(--brand-blue); font-weight: 700;
  }
  .offer__cta { font-size: 30px; letter-spacing: 0.3px; padding-left: 42px; line-height: 1.1; }
  .offer__deal { display: flex; align-items: center; gap: 6px; }
  .offer__percent { font-size: 60px; line-height: 1; letter-spacing: -1px; }
  .offer__terms { font-size: 25px; line-height: 1.02; text-transform: uppercase; }
  .offer__brand {
    margin-top: 34px; padding-left: 20px;
    font-size: 20px; font-weight: 700;
  }
  .social-square {
    position: absolute; right: 70px; top: 112px;
    width: 36px; height: 36px; border-radius: 4px; background: var(--brand-blue);
  }
  .back-info {
    position: absolute; right: 50px; bottom: 64px; text-align: right;
    font-size: 20px; line-height: 1.3;
  }
  .back-info__web { margin-bottom: 16px; }

  /* Front of card */
  .watermark-disc {
    position: absolute; right: -70px; bottom: -110px;
    width: 420px; height: 420px; border-radius: 50%;
    background: var(--brand-tint); opacity: 0.7;
  }
  .identity { position: absolute; left: 100px; top: 40px; }
  .identity__name {
    font-family: "Open Sans Condensed", "Open Sans", Arial, sans-serif;
    font-size: 52px; font-weight: 700; letter-spacing: -0.5px; line-height: 1;
  }
  .identity__tag-row { display: flex; align-items: center; gap: 12px; margin-top: 4px; margin-left: -4px; }
  .identity__dot { width: 30px; height: 30px; border-radius: 50%; background: var(--brand-blue); flex: none; }
  .identity__tagline {
    font-family: "Tinos", "Times New Roman", serif; font-style: italic; font-size: 22px;
  }
  .services {
    position: absolute; left: 96px; top: 162px; font-size: 21px; line-height: 1.3;
  }
  .contact {
    position: absolute; left: 68px; top: 268px; font-size: 21px; line-height: 1.4;
    list-style: none;
  }
  .contact__item { display: flex; align-items: center; gap: 8px; }
  .contact__icon { width: 18px; height: 18px; flex: none; }
  .contact__address { margin-top: 8px; margin-left: -14px; font-size: 22px; }
</style>
</head>
<body>
<main class="sheet">

  <section class="card card--back" aria-label="Card back">
    <span class="brand-disc" aria-hidden="true"></span>
    <div class="offer">
      <p class="offer__cta">Book Online</p>
      <div class="offer__deal">
        <span class="offer__percent">20</span>
        <span class="offer__terms">% Off<br>First Visit</span>
      </div>
      <p class="offer__brand">Open Range Wellness</p>
    </div>
    <span class="social-square" aria-label="Social page"></span>
    <div class="back-info">
      <p class="back-info__web">www.openrangewellnessnm.com</p>
      <p>We accept some insurances,<br>Worker's Comp and Personal Injury.</p>
    </div>
  </section>

  <section class="card card--front" aria-label="Card front">
    <span class="watermark-disc" aria-hidden="true"></span>
    <div class="identity">
      <h1 class="identity__name">Open Range Wellness</h1>
      <div class="identity__tag-row">
        <span class="identity__dot"></span>
        <p class="identity__tagline">Sports Therapy and Wellness Center</p>
      </div>
    </div>
    <p class="services">Specializing in<br>Medical, Sports Massage<br>Chiropractic and Acupuncture</p>
    <ul class="contact">
      <li class="contact__item">
        <svg class="contact__icon" viewBox="0 0 24 24" aria-hidden="true"><path fill="#263c96" d="M6.6 10.8a15.1 15.1 0 0 0 6.6 6.6l2.2-2.2a1 1 0 0 1 1-.25 11.4 11.4 0 0 0 3.6.57 1 1 0 0 1 1 1V20a1 1 0 0 1-1 1A17 17 0 0 1 3 4a1 1 0 0 1 1-1h3.5a1 1 0 0 1 1 1c0 1.25.2 2.45.57 3.6a1 1 0 0 1-.25 1z"/></svg>
        (505) 558-3927
      </li>
      <li class="contact__item">
        <svg class="contact__icon" viewBox="0 0 24 24" aria-hidden="true"><rect x="2" y="5" width="20" height="14" fill="none" stroke="#263c96" stroke-width="2"/><path d="M2 5l10 8 10-8" fill="none" stroke="#263c96" stroke-width="2"/></svg>
        info@openrangewellnessnm.com
      </li>
      <li class="contact__address">1450 Mesa Vista Rd, H2, Santa Fe, NM 87505</li>
    </ul>
  </section>

</main>
</body>
</html>
```